Annual Report Belvora 2025

Take a PowerPoint presentation and turn it into a info graphic type annual report, posters and flyers.

Annual report ideally no more than 8 pages.

Please use the colours and fonts in the attached brand guidelines.

We are looking for an infographic visually appealing piece.

```html
<!DOCTYPE html>
<html lang="en">
<head>
<meta charset="utf-8">
<title>Belvora Annual Report 2025</title>
<link rel="stylesheet" href="https://fonts.googleapis.com/css2?family=Inter:wght@400;500;600;700&family=Playfair+Display:ital,wght@0,400;0,700;0,800;1,400;1,700&display=swap">
<style>
:root{
  --board:#5e5e5e;
  --navy:#0a2d62;
  --navy-deep:#061d40;
  --navy-circle:#1b3f78;
  --green:#7aae33;
  --green-bright:#5fa12a;
  --forest:#1f4a33;
  --forest-dark:#1d3a22;
  --olive:#4a6e2a;
  --sage:#c9dca8;
  --cream:#f4f1e8;
  --ink:#1d2a44;
  --muted:#7a8396;
  --rule:#d9dde5;
  --white:#ffffff;
  --serif:'Playfair Display', Georgia, serif;
  --sans:'Inter', Arial, sans-serif;
}
*{margin:0;padding:0;box-sizing:border-box}
html,body{width:1200px;height:891px;overflow:hidden;background:var(--board)}
.board{position:absolute;left:0;top:0;width:2225px;height:1652px;transform:scale(0.5393);transform-origin:0 0;font-family:var(--sans);color:var(--ink)}
.page{position:absolute;background:var(--white);overflow:hidden}
.abs{position:absolute}
.band{position:absolute;left:0;top:0;right:0;height:130px;background:var(--navy);overflow:hidden}
.band .circle{position:absolute;border-radius:50%;background:var(--navy-circle);opacity:.55}
.kicker{position:absolute;left:33px;top:26px;font-family:var(--serif);font-size:6px;letter-spacing:.5px;color:#b8c4da;text-transform:uppercase}
.page-title{position:absolute;left:33px;font-family:var(--serif);font-weight:700;color:var(--white);line-height:1.08}
.page-sub{position:absolute;left:33px;font-size:8px;color:#b8c4da}
.serif{font-family:var(--serif)}
.green{color:var(--green)}
.navy{color:var(--navy)}
.label-caps{font-family:var(--serif);font-size:6.5px;font-weight:700;text-transform:uppercase;letter-spacing:.3px;color:var(--ink)}
.small{font-size:6.5px;color:var(--muted);line-height:1.35}
.pill{display:inline-block;background:var(--green);color:var(--white);font-size:7px;font-weight:600;padding:3px 9px;border-radius:9px}
.chip{display:inline-block;border:1px solid #6f9a7a;color:#cfe1d3;font-size:6px;padding:3px 7px;border-radius:8px;margin:0 3px 5px 0;text-transform:uppercase}
.outline-btn{position:absolute;border:1.5px solid var(--navy);border-radius:12px;color:var(--navy);font-size:8.5px;font-weight:500;padding:5px 14px;white-space:nowrap}
.fin-row{display:flex;justify-content:space-between;font-family:var(--serif);font-size:7.5px;color:var(--muted);line-height:13px}
.fin-total{display:flex;justify-content:space-between;font-size:8px;font-weight:500;color:var(--ink);border-top:1px solid #555;padding-top:4px;margin-top:3px}
.fin-head{font-size:8.5px;font-weight:600;color:var(--navy);border-bottom:1px solid #444;padding-bottom:4px;margin-bottom:6px}
.fin-sec{font-size:8.5px;font-weight:600;color:var(--green);margin:8px 0 5px}
.cover-stat{position:absolute;left:411px;width:241px;border-top:2px solid var(--navy)}
.cover-figure{font-family:var(--serif);font-size:32px;font-weight:700;line-height:36px;color:var(--navy);margin-bottom:3px}
.cover-stat .label-caps{font-size:5.5px;line-height:8px}
.cover-stat .small{font-size:6px;line-height:8px}
</style>
</head>
<body>
<div class="board">

<!-- Cover -->
<section class="page" style="left:48px;top:46px;width:679px;height:481px">
  <div class="abs" role="img" aria-label="Photo of people embracing, tinted in deep brand blue" style="left:0;top:0;width:346px;height:481px;background:linear-gradient(160deg,#123f86 0%,#0d3677 45%,#082a5f 100%)"></div>
  <div class="abs" style="left:346px;top:0;width:49px;height:481px;background:#06182f"></div>
  <div class="abs" style="left:34px;top:32px;display:flex;align-items:center;gap:8px">
    <span style="width:32px;height:32px;border-radius:50%;border:3px solid var(--white);display:block"></span>
    <span class="serif" style="font-size:36px;font-weight:700;color:var(--white)">Belvora</span>
  </div>
  <div class="abs serif" style="left:38px;top:104px;font-size:40px;font-weight:800;color:var(--green-bright)">2025</div>
  <div class="abs serif" style="left:38px;top:146px;font-size:34px;font-weight:700;color:var(--white);line-height:40px">Resilience<br>Through<br>Partnership</div>
  <div class="abs" style="left:38px;top:276px;width:172px;height:1px;background:#8ea3c6"></div>
  <div class="abs serif" style="left:38px;top:284px;font-size:15px;font-style:italic;color:var(--white)">Annual Report</div>

  <div class="cover-stat" style="top:76px;padding-top:10px">
    <div class="cover-figure">$100M+</div>
    <div class="label-caps">Assets Under Management</div>
    <div class="small">Historic milestone reached in 2025</div>
  </div>
  <div class="cover-stat" style="top:181px;padding-top:10px">
    <div class="cover-figure">$6M+</div>
    <div class="label-caps">Grants Facilitated</div>
    <div class="small">Supporting charities across Canada</div>
  </div>
  <div class="cover-stat" style="top:286px;padding-top:14px">
    <div class="cover-figure" style="line-height:32px">3</div>
    <div class="label-caps">New Services Launched</div>
    <div class="small">Money Market, Bookkeeping, Case Studies</div>
  </div>
</section>

<!-- Executive summary -->
<section class="page" style="left:757px;top:38px;width:703px;height:497px">
  <div class="band">
    <span class="circle" style="left:495px;top:-90px;width:200px;height:200px"></span>
    <span class="circle" style="left:300px;top:-130px;width:160px;height:160px;opacity:.3"></span>
  </div>
  <div class="kicker">02 — Executive Summary</div>
  <div class="page-title" style="top:38px;font-size:27px">A Year of Growth<br>&amp; Stewardship</div>
  <div class="page-sub" style="top:103px;font-size:7.5px">2025 marked a significant year for Belvora, grounded in trust and a shared commitment to thoughtful, values-driven generosity.</div>

  <div class="abs" style="left:63px;top:155px;width:4px;height:50px;background:var(--green)"></div>
  <p class="abs" style="left:78px;top:160px;width:450px;font-size:10.5px;line-height:15px;color:#333">Together with our fundholders, we surpassed $100 million in assets under management, facilitated more than $6 million in grants to charities across Canada, and deepened our service through new investment and bookkeeping solutions.</p>

  <div class="abs" style="left:60px;top:240px;width:182px;height:2px;background:#4d5d22"></div>
  <div class="abs" style="left:252px;top:240px;width:182px;height:2px;background:#8aa63d"></div>
  <div class="abs" style="left:445px;top:240px;width:182px;height:2px;background:#bcd290"></div>

  <svg class="abs" style="left:140px;top:258px" width="16" height="14" viewBox="0 0 16 14"><path d="M1 1V13H15M3 10L7 6L10 8L14 3" fill="none" stroke="#9aa3b3" stroke-width="1.2"/></svg>
  <svg class="abs" style="left:333px;top:256px" width="20" height="14" viewBox="0 0 20 14"><path d="M2 7L6 3H10L14 6L18 3M5 8L9 12L12 10L15 8" fill="none" stroke="#9aa3b3" stroke-width="1.2"/></svg>
  <svg class="abs" style="left:528px;top:257px" width="14" height="14" viewBox="0 0 14 14"><circle cx="7" cy="7" r="3" fill="none" stroke="#9aa3b3" stroke-width="1.2"/><circle cx="7" cy="7" r="6" fill="none" stroke="#9aa3b3" stroke-width="1.2" stroke-dasharray="2 1.5"/></svg>

  <div class="abs" style="left:85px;top:284px;width:130px;text-align:center"><div class="label-caps">Investment Milestone</div><div class="small" style="margin-top:5px">Surpassed $100M in assets under management—reflecting the trust placed in Belvora.</div></div>
  <div class="abs" style="left:278px;top:280px;width:130px;text-align:center"><div class="label-caps">Grantmaking Impact</div><div class="small" style="margin-top:8px">Facilitated more than $6M in grants to charities across Canada, responding to present needs.</div></div>
  <div class="abs" style="left:470px;top:282px;width:130px;text-align:center"><div class="label-caps">Service Expansion</div><div class="small" style="margin-top:6px">Strengthened investment solutions and introduced bookkeeping supports—practical tools.</div></div>

  <div class="abs serif" style="left:30px;top:330px;font-size:64px;font-weight:800;color:#c8d0dd;line-height:60px">“</div>
  <p class="abs serif" style="left:66px;top:382px;width:620px;font-size:11px;font-style:italic;font-weight:700;line-height:17px;color:var(--navy-deep)">Belvora is a Canadian public foundation committed to the faithful stewardship of generosity. We come alongside donors, families, and organizations to help translate charitable intent into thoughtful, lasting impact.</p>
  <div class="abs" style="left:260px;top:425px;font-size:10.5px;color:#333">— Belvora Mission Statement</div>
</section>

<!-- Key metrics -->
<section class="page" style="left:1498px;top:36px;width:704px;height:499px;background:var(--cream)">
  <div class="band">
    <span class="circle" style="left:360px;top:-90px;width:170px;height:170px"></span>
    <span class="circle" style="left:570px;top:-60px;width:160px;height:160px"></span>
  </div>
  <div class="kicker" style="top:28px">03 — Financial Highlights</div>
  <div class="page-title" style="top:44px;font-size:30px">2025 Key Metrics</div>
  <div class="page-sub" style="top:91px;font-size:7px;line-height:11px">Foundation financial highlights as of December 31, 2025.<br>Full audited statements prepared by Marden Hale LLP available at www.belvora.ca.</div>

  <div class="abs" style="left:57px;top:152px;width:265px;height:130px;background:var(--navy);border-radius:4px;padding:14px 12px">
    <div class="serif" style="color:var(--white);font-size:32px;line-height:34px">$104<span style="font-size:18px">M</span></div>
    <div style="color:#c3cde0;font-size:5.5px;text-transform:uppercase;margin-top:2px">Total Assets</div>
    <div style="color:#8fa1c2;font-size:6px;line-height:8px;margin-top:4px">Surpassing the $100M milestone for the first time,<br>a historic milestone grounded in donor trust.</div>
    <div style="border-top:1px solid #34508a;margin-top:6px;padding-top:6px;display:flex;gap:26px;color:var(--white)">
      <div><div class="serif" style="font-size:13px;font-weight:700">$3.9M</div><div style="font-size:4.5px;color:#8fa1c2">TOTAL REVENUE</div></div>
      <div><div class="serif" style="font-size:13px;font-weight:700">$1.1M</div><div style="font-size:4.5px;color:#8fa1c2">NET INCOME</div></div>
      <div><div class="serif" style="font-size:13px;font-weight:700">$1.4M</div><div style="font-size:4.5px;color:#8fa1c2">DONATIONS</div></div>
    </div>
  </div>

  <div class="abs" style="left:370px;top:152px;width:268px;height:40px;background:var(--white);border-top:2px solid var(--forest-dark);padding:10px 8px;display:flex;gap:14px">
    <span class="green" style="font-size:13px;font-weight:700">$</span>
    <div><div class="serif" style="font-size:14px;font-weight:700;color:var(--forest-dark);line-height:14px">$1.4M</div><div class="small" style="font-size:5.5px">Donations Received</div></div>
  </div>
  <div class="abs" style="left:370px;top:198px;width:268px;height:40px;background:var(--white);border-top:2px solid var(--forest-dark);padding:10px 8px;display:flex;gap:14px">
    <svg width="12" height="12" viewBox="0 0 12 12"><rect x="1" y="7" width="2" height="5" fill="#7aae33"/><rect x="5" y="4" width="2" height="8" fill="#7aae33"/><rect x="9" y="1" width="2" height="11" fill="#7aae33"/></svg>
    <div><div class="serif" style="font-size:14px;font-weight:700;color:var(--forest-dark);line-height:14px">$1.8M</div><div class="small" style="font-size:5.5px">Investment Income</div></div>
  </div>
  <div class="abs" style="left:370px;top:245px;width:268px;height:40px;background:var(--white);border-top:2px solid var(--forest-dark);padding:10px 8px;display:flex;gap:12px">
    <svg width="16" height="16" viewBox="0 0 16 16"><circle cx="8" cy="8" r="2.4" fill="none" stroke="#7aae33" stroke-width="1.3"/><circle cx="2.5" cy="2.5" r="1.6" fill="none" stroke="#7aae33"/><circle cx="13.5" cy="2.5" r="1.6" fill="none" stroke="#7aae33"/><circle cx="2.5" cy="13.5" r="1.6" fill="none" stroke="#7aae33"/><circle cx="13.5" cy="13.5" r="1.6" fill="none" stroke="#7aae33"/><path d="M4 4L6 6M12 4L10 6M4 12L6 10M12 12L10 10" stroke="#7aae33"/></svg>
    <div><div class="serif" style="font-size:14px;font-weight:700;color:var(--forest-dark);line-height:14px">$2.1M</div><div class="small" style="font-size:5.5px">Grants Disbursed</div></div>
  </div>

  <div class="abs" style="left:66px;top:312px;width:292px;height:168px;background:var(--white);border-radius:4px">
    <div class="serif" style="position:absolute;left:16px;top:10px;font-size:9px;font-weight:700">Asset Mix by Portfolio</div>
    <svg class="abs" style="left:16px;top:34px" width="110" height="110" viewBox="0 0 110 110">
      <g transform="rotate(-90 55 55)" fill="none" stroke-width="15">
        <circle cx="55" cy="55" r="40" stroke="#1d3a22" stroke-dasharray="78.9 251.3"/>
        <circle cx="55" cy="55" r="40" stroke="#4a6e2a" stroke-dasharray="74.4 251.3" stroke-dashoffset="-78.9"/>
        <circle cx="55" cy="55" r="40" stroke="#7aae33" stroke-dasharray="58.0 251.3" stroke-dashoffset="-153.3"/>
        <circle cx="55" cy="55" r="40" stroke="#c9dca8" stroke-dasharray="40.0 251.3" stroke-dashoffset="-211.3"/>
      </g>
      <text x="55" y="54" text-anchor="middle" font-family="Playfair Display, serif" font-size="8" font-weight="700" fill="#1d2a44">$104M</text>
      <text x="55" y="63" text-anchor="middle" font-family="Inter, sans-serif" font-size="4.5" fill="#7a8396">Total Assets</text>
    </svg>
    <div class="abs serif" style="left:140px;top:36px;width:130px;font-size:6.5px;line-height:15px;color:#444">
      <div style="display:flex;justify-content:space-between"><span><span style="display:inline-block;width:7px;height:7px;border-radius:50%;background:#1d3a22;margin-right:5px"></span>Canadian Equities</span><b>31.4%</b></div>
      <div style="display:flex;justify-content:space-between"><span><span style="display:inline-block;width:7px;height:7px;border-radius:50%;background:#4a6e2a;margin-right:5px"></span>Global Equities</span><b>29.6%</b></div>
      <div style="display:flex;justify-content:space-between"><span><span style="display:inline-block;width:7px;height:7px;border-radius:50%;background:#7aae33;margin-right:5px"></span>Fixed Income</span><b>23.1%</b></div>
      <div style="display:flex;justify-content:space-between"><span><span style="display:inline-block;width:7px;height:7px;border-radius:50%;background:#c9dca8;margin-right:5px"></span>Alternative</span><b>15.9%</b></div>
    </div>
  </div>

  <div class="abs" style="left:414px;top:310px;width:270px;height:170px;background:var(--white);border-radius:4px">
    <div class="serif" style="position:absolute;left:13px;top:2px;font-size:9px;font-weight:700">Charitable Distributions ($M)</div>
    <svg class="abs" style="left:0;top:24px" width="270" height="140" viewBox="0 0 270 140">
      <g font-family="Playfair Display, serif" font-size="5" fill="#7a8396">
        <text x="0" y="11">2019</text><text x="0" y="30">2020</text><text x="0" y="49">2021</text><text x="0" y="68">2022</text><text x="0" y="87">2023</text><text x="0" y="106">2024</text><text x="0" y="125">2025</text>
      </g>
      <g fill="#eeece6">
        <rect x="16" y="4" width="175" height="12"/><rect x="16" y="23" width="175" height="12"/><rect x="16" y="42" width="175" height="12"/><rect x="16" y="61" width="175" height="12"/><rect x="16" y="80" width="175" height="12"/><rect x="16" y="99" width="175" height="12"/><rect x="16" y="118" width="175" height="12"/>
      </g>
      <rect x="16" y="4" width="66" height="12" fill="#c9dca8"/>
      <rect x="16" y="23" width="77" height="12" fill="#a9c874"/>
      <rect x="16" y="42" width="92" height="12" fill="#7aae33"/>
      <rect x="16" y="61" width="103" height="12" fill="#5f8a2c"/>
      <rect x="16" y="80" width="117" height="12" fill="#3f5f24"/>
      <rect x="16" y="99" width="136" height="12" fill="#2b3f20"/>
      <rect x="16" y="118" width="175" height="12" fill="#1a1f1c"/>
      <g font-family="Playfair Display, serif" font-size="5.5" font-weight="700" fill="#fff" text-anchor="end">
        <text x="78" y="12">$1.8M</text><text x="89" y="31">$2.1M</text><text x="104" y="50">$2.5M</text><text x="115" y="69">$2.8M</text><text x="129" y="88">$3.2M</text><text x="148" y="107">$3.7M</text><text x="187" y="126">$6.0M</text>
      </g>
    </svg>
  </div>
</section>

<!-- Grants -->
<section class="page" style="left:36px;top:577px;width:704px;height:499px">
  <div class="band">
    <span class="circle" style="left:445px;top:-40px;width:160px;height:160px"></span>
    <span class="circle" style="left:170px;top:-110px;width:140px;height:140px;opacity:.3"></span>
  </div>
  <div class="kicker" style="top:28px">04 — Grants &amp; Giving</div>
  <div class="page-title" style="top:47px;font-size:28px">Impact Through<br>Purposeful Giving</div>

  <div class="abs serif navy" style="left:40px;top:152px;font-size:22px;font-weight:700">Our Grant Programs</div>
  <div class="abs" style="left:50px;top:202px;width:290px">
    <div style="border-left:2px solid var(--navy);padding-left:12px;height:36px;margin-bottom:14px"><div class="serif navy" style="font-size:9.5px;font-weight:700">Partner Grants Program</div><div style="font-size:7.5px;color:var(--navy);margin-top:4px">Supporting projects that address critical social &amp; environmental needs.</div></div>
    <div style="border-left:2px solid var(--navy);padding-left:12px;height:36px;margin-bottom:14px"><div class="serif navy" style="font-size:9.5px;font-weight:700">Daniel Ashcroft Social Justice Fund</div><div style="font-size:7.5px;color:var(--navy);margin-top:4px">Promoting social justice, equity, and systemic change across Canada.</div></div>
    <div style="border-left:2px solid var(--navy);padding-left:12px;height:36px;margin-bottom:14px"><div class="serif navy" style="font-size:9.5px;font-weight:700">Owen Larkin Legacy Fund</div><div style="font-size:7.5px;color:var(--navy);margin-top:4px">Carrying forward a legacy of generosity, faith, and community values.</div></div>
    <div style="border-left:2px solid var(--navy);padding-left:12px;height:36px"><div class="serif navy" style="font-size:9.5px;font-weight:700">Donor Advised Funds (DAFs)</div><div style="font-size:7.5px;color:var(--navy);margin-top:4px">Flexible, intention-driven giving with immediate tax receipt options.</div></div>
  </div>
  <div class="abs" style="left:41px;top:409px;width:292px;height:38px;background:var(--green);border-radius:3px;display:flex;align-items:center;justify-content:space-between;padding:0 16px">
    <span class="serif" style="color:var(--white);font-size:8.5px;font-weight:700;text-transform:uppercase">Total Grants 2025</span>
    <span class="serif" style="color:var(--white);font-size:22px;font-weight:700">$6M+</span>
  </div>

  <div class="abs navy" style="left:444px;top:154px;font-size:12px;font-weight:600">Guiding Principles</div>
  <div class="abs" style="left:366px;top:189px;width:310px;font-size:7.5px;color:#333">
    <div style="display:flex;align-items:center;gap:6px;height:26px;border-bottom:1px solid #eee"><span style="width:15px;height:15px;border-radius:50%;background:var(--green);color:#fff;font-size:5px;display:flex;align-items:center;justify-content:center">1</span>Respect human rights and dignity</div>
    <div style="display:flex;align-items:center;gap:6px;height:26px;border-bottom:1px solid #eee"><span style="width:15px;height:15px;border-radius:50%;background:var(--green);color:#fff;font-size:5px;display:flex;align-items:center;justify-content:center">2</span>Respect workers' rights</div>
    <div style="display:flex;align-items:center;gap:6px;height:26px;border-bottom:1px solid #eee"><span style="width:15px;height:15px;border-radius:50%;background:var(--green);color:#fff;font-size:5px;display:flex;align-items:center;justify-content:center">3</span>Enhance economic and social justice</div>
    <div style="display:flex;align-items:center;gap:6px;height:26px;border-bottom:1px solid #eee"><span style="width:15px;height:15px;border-radius:50%;background:var(--green);color:#fff;font-size:5px;display:flex;align-items:center;justify-content:center">4</span>Operate in an environmentally sustainable manner</div>
    <div style="display:flex;align-items:center;gap:6px;height:26px"><span style="width:15px;height:15px;border-radius:50%;background:var(--green);color:#fff;font-size:5px;display:flex;align-items:center;justify-content:center">5</span>Support a global culture of peace</div>
  </div>
  <div class="abs" style="left:364px;top:338px;width:278px;height:72px;border:1px solid #999;border-radius:3px;padding:8px 12px">
    <div style="font-size:8.5px;font-weight:500;color:#222">Social Impact Focus Areas</div>
    <ul style="list-style:none;font-size:6.5px;color:var(--navy);margin-top:6px;line-height:12px">
      <li>● &nbsp;Elimination of poverty in Canada</li>
      <li>● &nbsp;Reconciliation with Indigenous peoples</li>
      <li>● &nbsp;Promotion of environmental sustainability</li>
    </ul>
  </div>
</section>

<!-- Investing -->
<section class="page" style="left:767px;top:577px;width:704px;height:499px">
  <div class="band">
    <span class="circle" style="left:360px;top:-70px;width:150px;height:150px"></span>
    <span class="circle" style="left:560px;top:-20px;width:170px;height:170px"></span>
  </div>
  <div class="kicker" style="top:28px">05 — Investment Solutions</div>
  <div class="page-title" style="top:43px;font-size:27px">Faith-Based<br>Responsible Investing</div>
  <div class="page-sub" style="top:106px;font-size:7.5px">Three portfolios tailored for congregations and charitable organizations.</div>

  <div class="abs" style="left:84px;top:161px;width:163px;height:204px;background:var(--forest);border-radius:3px;padding:16px 14px">
    <span class="pill" style="font-size:6.5px">NEW IN 2025</span>
    <div style="color:#fff;font-size:13px;font-weight:500;margin-top:8px;line-height:16px">Money Market<br>Portfolio</div>
    <div style="color:#8fb09a;font-size:6px;line-height:8px;margin-top:6px">Launched in 2025 to provide churches and charities with a prudent, accessible solution for stewarding short-term funds. Focused on capital preservation, stability, and liquidity.</div>
    <div style="color:#8fb09a;font-size:6px;letter-spacing:1px;margin:12px 0 6px">FOCUS</div>
    <span class="chip">Capital Preservation</span><span class="chip">Stability</span><span class="chip">Liquidity</span>
  </div>
  <div class="abs" style="left:261px;top:161px;width:163px;height:204px;background:var(--forest);border-radius:3px;padding:16px 14px">
    <span class="pill" style="font-size:6.5px">BALANCED GROWTH</span>
    <div style="color:#fff;font-size:13px;font-weight:500;margin-top:16px">Balanced Portfolio</div>
    <div style="color:#8fb09a;font-size:6px;line-height:8px;margin-top:14px">A diversified portfolio offering a balance between capital growth and income generation, aligned with ESG screening and responsible investing principles.</div>
    <div style="color:#8fb09a;font-size:6px;letter-spacing:1px;margin:20px 0 6px">FOCUS</div>
    <span class="chip">Income</span><span class="chip">Growth</span><span class="chip">ESG Screened</span>
  </div>
  <div class="abs" style="left:439px;top:161px;width:163px;height:204px;background:var(--forest);border-radius:3px;padding:16px 14px">
    <span class="pill" style="font-size:6.5px">LONG-TERM GROWTH</span>
    <div style="color:#fff;font-size:13px;font-weight:500;margin-top:16px">Growth Portfolio</div>
    <div style="color:#8fb09a;font-size:6px;line-height:8px;margin-top:14px">Designed for organizations with a longer time horizon, emphasizing capital appreciation while maintaining responsible investing practices.</div>
    <div style="color:#8fb09a;font-size:6px;letter-spacing:1px;margin:20px 0 6px">FOCUS</div>
    <span class="chip">Capital Growth</span><span class="chip">Long-Term</span><span class="chip">Faith-Aligned</span>
  </div>

  <div class="abs" style="left:56px;top:406px;display:flex;gap:20px;font-size:7px;color:#222;line-height:9px">
    <div style="display:flex;gap:6px"><span style="width:5px;height:22px;background:var(--green)"></span>Global Principles for<br>Responsible Investment</div>
    <div style="display:flex;gap:6px"><span style="width:5px;height:22px;background:#111"></span>People &amp; Capital<br>Stewardship Coalition</div>
    <div style="display:flex;gap:6px"><span style="width:5px;height:22px;background:var(--sage)"></span>Sustainability<br>Standards Forum</div>
    <div style="display:flex;gap:6px"><span style="width:5px;height:22px;background:#7c8aa3"></span>Workforce<br>Transparency Initiative</div>
    <div style="display:flex;gap:6px"><span style="width:5px;height:22px;background:#b8bfcc"></span>Charter on Rights of<br>Indigenous Peoples</div>
  </div>
</section>

<!-- Highlights -->
<section class="page" style="left:1498px;top:577px;width:704px;height:499px">
  <div class="band">
    <span class="circle" style="left:360px;top:-70px;width:150px;height:150px"></span>
    <span class="circle" style="left:560px;top:-20px;width:170px;height:170px"></span>
  </div>
  <div class="kicker" style="top:39px">06 — 2025 Highlights</div>
  <div class="page-title" style="top:55px;font-size:32px">2025 Highlights</div>
  <div class="page-sub" style="top:106px;font-size:7.5px">Three major milestones expanding Belvora's capacity to serve the charitable sector.</div>

  <div class="abs" style="left:107px;top:164px;width:210px">
    <span class="pill" style="font-size:6px;padding:2px 9px">Investment</span>
    <div class="navy" style="font-size:15px;font-weight:500;margin-top:6px">New Money Market Portfolio</div>
    <div class="small" style="margin-top:6px;width:180px;font-size:6px">Launched to provide churches and charities with a prudent, accessible solution for stewarding short-term funds. It is the most conservative option in the Belvora investment suite, ideal for managing reserves and preparing for future ministry initiatives.</div>
  </div>
  <div class="outline-btn" style="left:108px;top:268px">3 Portfolio options now available</div>

  <div class="abs" style="left:387px;top:164px;width:210px">
    <span class="pill" style="font-size:6px;padding:2px 9px">Milestone</span>
    <div class="navy" style="font-size:15px;font-weight:500;margin-top:6px">$100 Million in Assets</div>
    <div class="small" style="margin-top:6px;width:180px;font-size:6px">Belvora surpassed $100 million in assets under management—an important milestone grounded in donor trust and a shared commitment to generosity. We steward these funds with a long-term perspective, seeking to preserve and grow capital.</div>
  </div>
  <div class="outline-btn" style="left:386px;top:268px">$104M Total assets as of Dec 31, 2025</div>

  <div class="abs" style="left:110px;top:321px;width:210px">
    <span class="pill" style="font-size:6px;padding:2px 9px">Knowledge</span>
    <div class="navy" style="font-size:15px;font-weight:500;margin-top:6px">New Case Studies Series</div>
    <div class="small" style="margin-top:6px;width:180px;font-size:6px">Released a new series of case studies reflecting the heart of Belvora's work—faithful stewardship through thoughtful and purposeful giving. These stories offer a window into how donor intent is carefully discerned and carried forward, creating tangible community impact.</div>
  </div>
  <div class="outline-btn" style="left:112px;top:436px">New Series released in 2025</div>

  <div class="abs" style="left:392px;top:321px;width:210px">
    <span class="pill" style="font-size:6px;padding:2px 9px">Services</span>
    <div class="navy" style="font-size:15px;font-weight:500;margin-top:6px">Bookkeeping Services</div>
    <div class="small" style="margin-top:6px;width:180px;font-size:6px">Expanded service offerings with the introduction of dedicated bookkeeping services—an extension of Belvora's commitment to faithful and holistic stewardship. Sound financial practices are foundational to sustainable ministry and charitable impact.</div>
  </div>
  <div class="outline-btn" style="left:382px;top:435px">New Service launched to reduce admin burden</div>
</section>

<!-- Financial statements -->
<section class="page" style="left:36px;top:1120px;width:704px;height:499px">
  <div class="band">
    <span class="circle" style="left:540px;top:-40px;width:160px;height:160px"></span>
    <span class="circle" style="left:80px;top:-120px;width:130px;height:130px;opacity:.3"></span>
  </div>
  <div class="kicker" style="top:28px">07 — Financial Statements</div>
  <div class="page-title" style="top:45px;font-size:27px">Foundation Financial<br>Highlights</div>

  <div class="abs" style="left:68px;top:152px;width:270px">
    <div class="fin-head">Statement of Operations (000s)</div>
    <div class="fin-row"><span>Donations</span><span>1,403</span></div>
    <div class="fin-row"><span>Investment Gain</span><span>1,791</span></div>
    <div class="fin-row"><span>Other Income</span><span>733</span></div>
    <div class="fin-total"><span>Total Income</span><span class="serif">3,927</span></div>
    <div class="fin-row"><span>Expenses</span><span>656</span></div>
    <div class="fin-row"><span>Grants</span><span>2,143</span></div>
    <div class="fin-total"><span>Reinvested Income</span><span class="serif">1,128</span></div>
  </div>

  <div class="abs" style="left:380px;top:152px;width:255px">
    <div class="fin-head">Statement of Financial Position (000s)</div>
    <div class="fin-sec">Assets</div>
    <div class="fin-row"><span>Cash</span><span>14,981</span></div>
    <div class="fin-row"><span>Accounts Receivable</span><span>156</span></div>
    <div class="fin-row"><span>Donated Life Insurance</span><span>13</span></div>
    <div class="fin-row"><span>Investments</span><span>88,958</span></div>
    <div class="fin-total"><span>Total</span><span class="serif">104,108</span></div>
    <div class="fin-sec" style="margin-top:12px">Liabilities</div>
    <div class="fin-row"><span>Accounts Payable</span><span>926</span></div>
    <div class="fin-row"><span>Partner Fund Income Due</span><span>3,868</span></div>
    <div class="fin-row"><span>Partner Fund capital</span><span>67,742</span></div>
    <div class="fin-sec" style="margin-top:12px">Fund Balances</div>
    <div class="fin-row" style="border-top:1px solid #ccc;padding-top:2px"><span>Endowed</span><span>23,367</span></div>
    <div class="fin-row"><span>Restricted</span><span>8,145</span></div>
    <div class="fin-row"><span>Unrestricted</span><span>60</span></div>
    <div class="fin-total"><span>Total</span><span class="serif">104,108</span></div>
  </div>
</section>

<!-- Closing -->
<section class="page" style="left:767px;top:1120px;width:704px;height:499px;background:var(--navy)">
  <span class="abs" style="left:-40px;top:-70px;width:420px;height:420px;border-radius:50%;background:var(--navy-circle);opacity:.45"></span>
  <div class="abs serif" style="left:38px;top:56px;font-size:50px;font-weight:800;line-height:48px;color:var(--white)">Values<br><span style="color:var(--green)">Driving</span><br>Values</div>
  <div class="abs" style="left:38px;top:227px;width:218px;height:2px;background:#cfd7e6"></div>
  <p class="abs" style="left:38px;top:238px;width:215px;font-size:8px;line-height:14px;color:var(--white)">Belvora remains committed to serving as a steady partner—guiding resources with wisdom and accountability so that each act of giving is aligned with conviction and meaningful community impact.</p>
  <div class="abs" style="left:38px;top:318px;color:var(--white)"><div class="serif green" style="font-size:20px;font-weight:700">$100M+</div><div style="font-size:6.5px">Assets</div></div>
  <div class="abs" style="left:166px;top:318px;color:var(--white)"><div class="serif green" style="font-size:20px;font-weight:700">$6M+</div><div style="font-size:6.5px">Grants</div></div>
  <div class="abs" style="left:294px;top:320px;color:var(--white)"><div class="serif green" style="font-size:20px;font-weight:700;line-height:22px">3</div><div style="font-size:6.5px">New Services</div></div>

  <div class="abs" style="left:364px;top:40px;width:1px;height:400px;background:#1f4380"></div>
  <div class="abs serif" style="left:390px;top:48px;font-size:12px;font-weight:700;color:var(--white)">GET IN TOUCH</div>
  <div class="abs" style="left:390px;top:68px;width:218px;height:1px;background:#4b6799"></div>
  <div class="abs" style="left:402px;top:100px;color:var(--white);font-size:8px;border-left:2px solid #fff;padding-left:7px">info@belvora.ca<div style="font-size:5.5px;color:#6f86b0">Email</div></div>
  <div class="abs" style="left:402px;top:153px;color:var(--white);font-size:8px;border-left:2px solid #fff;padding-left:7px">888.555.0142<div style="font-size:5.5px;color:#6f86b0">Toll-Free</div></div>
  <div class="abs" style="left:402px;top:205px;color:var(--white);font-size:8px;border-left:2px solid #fff;padding-left:7px">www.belvora.ca<div style="font-size:5.5px;color:#6f86b0">Website</div></div>
  <div class="abs" style="left:402px;top:258px;color:var(--white);font-size:8px;border-left:2px solid #fff;padding-left:7px">120 Harlow St E, Kitchener ON N2A 1B4<div style="font-size:5.5px;color:#6f86b0">Address</div></div>

  <div class="abs" style="left:406px;top:362px;display:flex;align-items:center;gap:10px">
    <span style="width:40px;height:40px;border-radius:50%;border:3px solid var(--white);display:block"></span>
    <span class="serif" style="font-size:40px;font-weight:700;color:var(--white)">Belvora</span>
  </div>

  <div class="abs" style="left:0;bottom:0;width:704px;height:40px;background:var(--green);display:flex;align-items:center;padding:0 36px;color:var(--white)">
    <span style="width:14px;height:14px;border-radius:50%;border:2px solid var(--white);margin-right:5px"></span>
    <span class="serif" style="font-size:16px;font-weight:700">Belvora</span>
    <span style="font-size:7.5px;margin-left:38px">Charitable Registration #: 81234 5678 RR0001</span>
    <span style="font-size:9.5px;margin-left:auto">Annual Report 2025</span>
  </div>
</section>

</div>
</body>
</html>
```